Professional & attention grabbing.

A business card design, front and back. I already have a logo I will attach, but I am open to something new as well.
Things to include:
Name:
Title:
Phone:
Email:
Wanting something that is professional but attention grabbing.
Also we do a lot of work using drones on natural gas pipelines (leading the future)if you want to include any of that. I'm open to ideas.
Target Market(s)
Natural gas transmission industry / greenhouse gas mitigation industry
Industry/Entity Type
Business
Contact Information for Business Card
All details have been conveyed above.
Colors
Designer to choose colors to be used in the design.
Look and feel
Each slider illustrates characteristics of the customer's brand and the style your logo design should communicate.

```html
<!DOCTYPE html>
<html lang="en">
<head>
<meta charset="utf-8">
<title>Kestrel Line Inspections — Business Card</title>
<link rel="stylesheet" href="https://fonts.googleapis.com/css2?family=Montserrat:wght@800&family=Open+Sans:wght@400;600&display=swap">
<style>
  :root {
    --backdrop: #e8e6e3;
    --card-white: #ffffff;
    --charcoal: #38383b;
    --brand-red: #c1272d;
    --rule-grey: #8a8a8a;
    --text-light: #ffffff;
    --text-muted: #d9d9d9;
  }
  * { margin: 0; padding: 0; box-sizing: border-box; }
  html, body {
    width: 1200px; height: 1135px; overflow: hidden;
    background: var(--backdrop);
  }
  .sheet {
    position: relative; width: 1200px; height: 1135px;
  }
  .card {
    position: absolute; left: 260px;
    width: 680px; height: 406px;
    background: var(--card-white);
    overflow: hidden;
    box-shadow: 0 2px 6px rgba(0,0,0,0.12);
  }
  .card--front { top: 90px; }
  .card--back { top: 625px; }
  .card__swoosh {
    position: absolute; inset: 0; width: 680px; height: 406px;
  }
  .contact-panel {
    position: absolute; left: 0; top: 0; width: 350px; height: 406px;
    background: var(--charcoal);
  }
  .holder-name {
    position: absolute; left: 28px; top: 153px;
    font: 800 30px/1 "Montserrat", sans-serif;
    color: var(--text-light);
  }
  .holder-title {
    position: absolute; left: 28px; top: 206px;
    font: 400 16px/1 "Open Sans", sans-serif;
    color: var(--text-muted);
  }
  .contact-line {
    position: absolute; left: 28px;
    display: flex; align-items: center; gap: 10px;
    font: 400 16px/1 "Open Sans", sans-serif;
    color: var(--text-light);
  }
  .contact-line--phone { top: 299px; }
  .contact-line--email { top: 349px; }
  .contact-icon { width: 22px; height: 22px; flex: none; }
  .brand {
    position: absolute;
    display: flex; align-items: center;
    color: var(--charcoal);
    font-family: "Montserrat", sans-serif; font-weight: 800;
  }
  .brand__square { background: var(--brand-red); flex: none; }
  .brand__name { display: flex; flex-direction: column; }
  .brand__word { line-height: 0.9; letter-spacing: -0.5px; }
  .brand__tag { letter-spacing: 0.3px; }
  .card--front .brand { left: 400px; top: 150px; gap: 12px; }
  .card--front .brand__square { width: 30px; height: 30px; }
  .card--front .brand__word { font-size: 46px; }
  .card--front .brand__tag { font-size: 9.5px; margin-top: 4px; }
  .card--back .brand { left: 183px; top: 148px; gap: 18px; }
  .card--back .brand__square { width: 44px; height: 44px; }
  .card--back .brand__word { font-size: 70px; }
  .card--back .brand__tag { font-size: 14.5px; margin-top: 6px; }
</style>
</head>
<body>
<main class="sheet">

  <section class="card card--front" aria-label="Business card front">
    <div class="contact-panel"></div>
    <svg class="card__swoosh" viewBox="0 0 680 406" aria-hidden="true">
      <path d="M-5,93 H258 Q308,93 340,52 L385,-5" fill="none" stroke="var(--rule-grey)" stroke-width="3"/>
      <path d="M-5,79 H254 Q298,79 328,42 L372,-5" fill="none" stroke="var(--brand-red)" stroke-width="22"/>
      <path d="M685,331 H428 Q380,331 356,366 L334,411" fill="none" stroke="var(--rule-grey)" stroke-width="3"/>
      <path d="M685,344 H432 Q392,344 372,376 L354,411" fill="none" stroke="var(--brand-red)" stroke-width="22"/>
    </svg>

    <h1 class="holder-name">Your Name</h1>
    <p class="holder-title">Title</p>

    <p class="contact-line contact-line--phone">
      <svg class="contact-icon" viewBox="0 0 22 22" aria-hidden="true">
        <circle cx="11" cy="11" r="11" fill="var(--brand-red)"/>
        <path d="M8,6 L10,6 L10.6,8.6 L9.4,9.6 Q10.4,12 12.4,12.8 L13.4,11.6 L16,12.2 L16,14.2 Q15.6,15.6 14,15.4 Q8.4,14.2 6.8,8 Q6.6,6.4 8,6 Z" fill="#fff"/>
      </svg>
      <span>555 010 2468</span>
    </p>
    <p class="contact-line contact-line--email">
      <svg class="contact-icon" viewBox="0 0 22 22" aria-hidden="true">
        <circle cx="11" cy="11" r="11" fill="var(--brand-red)"/>
        <rect x="6" y="7.5" width="10" height="7" rx="0.8" fill="#fff"/>
        <path d="M6.4,8 L11,11.4 L15.6,8" fill="none" stroke="var(--brand-red)" stroke-width="1"/>
      </svg>
      <span>name@example.com</span>
    </p>

    <div class="brand">
      <span class="brand__square"></span>
      <span class="brand__name">
        <span class="brand__word">KESTREL</span>
        <span class="brand__tag">LINE INSPECTIONS</span>
      </span>
    </div>
  </section>

  <section class="card card--back" aria-label="Business card back">
    <svg class="card__swoosh" viewBox="0 0 680 406" aria-hidden="true">
      <path d="M-5,93 H258 Q308,93 340,52 L385,-5" fill="none" stroke="var(--rule-grey)" stroke-width="3"/>
      <path d="M-5,79 H254 Q298,79 328,42 L372,-5" fill="none" stroke="var(--brand-red)" stroke-width="22"/>
      <path d="M685,331 H428 Q380,331 356,366 L334,411" fill="none" stroke="var(--rule-grey)" stroke-width="3"/>
      <path d="M685,344 H432 Q392,344 372,376 L354,411" fill="none" stroke="var(--brand-red)" stroke-width="22"/>
    </svg>

    <div class="brand">
      <span class="brand__square"></span>
      <span class="brand__name">
        <span class="brand__word">KESTREL</span>
        <span class="brand__tag">LINE INSPECTIONS</span>
      </span>
    </div>
  </section>

</main>
</body>
</html>
```